Industrial Professional Business Card Design (Vantrel Systems)

Would like professional looking business cards. Not too busy leaning towards minimal. Should have a slogan like:
"Industrial Automation and Control".

We are a tech company that programs industrial PLC computers. We also develop custom hardware solutions. Please use the logo for inspiration.

Target Market(s)

Mining, industrial, processing, automation, factory

Industry/Entity Type

Engineering

Contact Information for Business Card

Name, phone, email, website. job title.

Font styles to use
Other font styles liked:
• droid sans

Requirements
Must have
• Use colours that go well with the logo. Not too busy design.

```html
<!DOCTYPE html>
<html lang="en">
<head>
<meta charset="utf-8">
<title>Vantrel Systems – Business Card</title>
<link href="https://fonts.googleapis.com/css2?family=Noto+Sans:wght@400;500;600&display=swap" rel="stylesheet">
<style>
  :root {
    --navy: #1c2a5e;
    --navy-deep: #1a2352;
    --steel-blue: #1e6e95;
    --band-blue: #1d5f8c;
    --orange: #f26a21;
    --white: #ffffff;
    --paper: #ffffff;
    --backdrop: #e9e6e1;
    --rule: #1c3a6a;
  }
  * { box-sizing: border-box; margin: 0; padding: 0; }
  html, body { width: 1200px; height: 800px; overflow: hidden; }
  body {
    background: var(--backdrop);
    font-family: "Noto Sans", sans-serif;
    display: flex;
    align-items: center;
    justify-content: center;
    gap: 40px;
  }
  .card {
    position: relative;
    width: 540px;
    height: 309px;
    border-radius: 4px;
    overflow: hidden;
    box-shadow: 0 6px 18px rgba(0,0,0,0.18);
  }

  /* Front side */
  .card-front {
    background: radial-gradient(ellipse at 50% 45%, var(--steel-blue) 0%, #1d4f82 38%, var(--navy-deep) 80%);
    display: flex;
    flex-direction: column;
    align-items: center;
    justify-content: center;
    color: var(--white);
  }
  .brand {
    display: flex;
    align-items: center;
    gap: 12px;
  }
  .brand-dot {
    width: 22px; height: 22px;
    border-radius: 50%;
    background: var(--orange);
    flex: none;
  }
  .brand-name {
    font-weight: 500;
    font-size: 34px;
    letter-spacing: 0.2px;
  }
  .card-front .brand-name { color: var(--white); }
  .front-slogan {
    margin-top: 8px;
    font-size: 12px;
    font-weight: 500;
    letter-spacing: 0.3px;
  }

  /* Back side */
  .card-back { background: var(--paper); color: var(--navy); }
  .back-brand {
    position: absolute;
    left: 36px;
    top: 120px;
  }
  .back-brand .brand-name { color: var(--navy); font-size: 30px; }
  .divider-blue {
    position: absolute;
    left: 36px; top: 172px;
    width: 300px; height: 1.5px;
    background: var(--rule);
  }
  .divider-blue::after, .divider-orange::before {
    content: "";
    position: absolute;
    top: -2.5px;
    width: 6px; height: 6px;
    border-radius: 50%;
  }
  .divider-blue::after { right: -3px; background: var(--rule); }
  .divider-orange {
    position: absolute;
    left: 344px; top: 172px;
    width: 164px; height: 1.5px;
    background: var(--orange);
  }
  .divider-orange::before { left: -3px; background: var(--orange); }

  .person {
    position: absolute;
    left: 36px; top: 205px;
    border-top: 1.5px solid var(--rule);
    padding-top: 6px;
  }
  .person-name { font-size: 20px; font-weight: 600; color: var(--navy); line-height: 1.1; }
  .person-title { font-size: 11px; font-weight: 500; color: var(--orange); }

  .contacts {
    position: absolute;
    right: 32px; top: 84px;
    list-style: none;
    text-align: right;
  }
  .contacts li {
    display: flex;
    justify-content: flex-end;
    align-items: center;
    gap: 8px;
    font-size: 11.5px;
    color: var(--navy);
    line-height: 22px;
  }
  .contact-icon {
    width: 14px; height: 14px;
    flex: none;
  }

  .slogan-band {
    position: absolute;
    right: 0; bottom: 22px;
    width: 300px; height: 30px;
    background: linear-gradient(90deg, var(--band-blue), var(--navy));
    clip-path: polygon(20px 0, 100% 0, 100% 100%, 0 100%);
    color: var(--white);
    font-size: 11px;
    font-weight: 500;
    display: flex;
    align-items: center;
    justify-content: center;
    padding-left: 20px;
  }
</style>
</head>
<body>

  <section class="card card-front" aria-label="Business card front">
    <div class="brand">
      <span class="brand-dot"></span>
      <span class="brand-name">Vantrel Systems</span>
    </div>
    <p class="front-slogan">Industrial Automation and Control</p>
  </section>

  <section class="card card-back" aria-label="Business card back">
    <div class="brand back-brand">
      <span class="brand-dot"></span>
      <span class="brand-name">Vantrel Systems</span>
    </div>

    <ul class="contacts">
      <li>(03) 5550 1842
        <svg class="contact-icon" viewBox="0 0 14 14" aria-hidden="true">
          <circle cx="7" cy="7" r="6.3" fill="none" stroke="#f26a21" stroke-width="1.2"/>
          <path d="M4.6 4.2c.4-.4.8-.3 1 .1l.5.9c.2.3.1.6-.1.8l-.3.3c.3.7.9 1.3 1.6 1.6l.3-.3c.2-.2.5-.3.8-.1l.9.5c.4.2.5.6.1 1-.6.6-1.4.7-2.2.3C6 8.7 5.3 8 4.7 6.6c-.4-.8-.3-1.7-.1-2.4z" fill="#f26a21"/>
        </svg>
      </li>
      <li>dana@vantrelsystems.com
        <svg class="contact-icon" viewBox="0 0 14 14" aria-hidden="true">
          <circle cx="7" cy="7" r="6.3" fill="none" stroke="#f26a21" stroke-width="1.2"/>
          <rect x="3.8" y="4.8" width="6.4" height="4.4" rx="0.6" fill="#f26a21"/>
          <path d="M3.9 5l3.1 2.3L10.1 5" fill="none" stroke="#fff" stroke-width="0.8"/>
        </svg>
      </li>
      <li>www.vantrelsystems.com
        <svg class="contact-icon" viewBox="0 0 14 14" aria-hidden="true">
          <circle cx="7" cy="7" r="6.3" fill="none" stroke="#f26a21" stroke-width="1.2"/>
          <circle cx="7" cy="7" r="3.3" fill="none" stroke="#f26a21" stroke-width="0.9"/>
          <ellipse cx="7" cy="7" rx="1.4" ry="3.3" fill="none" stroke="#f26a21" stroke-width="0.8"/>
          <path d="M3.7 7h6.6" stroke="#f26a21" stroke-width="0.8"/>
        </svg>
      </li>
    </ul>

    <div class="divider-blue"></div>
    <div class="divider-orange"></div>

    <div class="person">
      <p class="person-name">Dana Whitlock</p>
      <p class="person-title">Managing Director</p>
    </div>

    <div class="slogan-band">Industrial Automation and Control</div>
  </section>

</body>
</html>
```